Photography business - business card design quick turn around

Create a business card design for me please. I actually need the final design back before the end of Sunday 13th May 7pm GMT. Sorry for the short notice.

Photoshop artwork template uploaded with artwork guidelines including printer profiles and other mandatory specifications. Only one side of the business card is required as the other side will be an image.

The design is required as an unflattened PSD file so that I can edit the text if I need to.

My brand colours are white and the teal you see in the logo. Occasionally I also use a dark grey on my website (I don't mind the shade of grey as appreciate grey on teal would be a different grey, to the grey I use on white on the website, so just use a shade of grey that matches). Font can be as the font for the logo or if you prefer I am open to another sans serif, easily legible font. Ideally font size will be 12+.Please do not use capital letters for text. I prefer everything to be lower case, if possible.

Thank you.

Mira

Target Market(s)

Other business owners who may refer me and families

Industry/Entity Type

Photographer

Contact Information for Business Card

Silver Lantern Photography Logo
Sub text: family portraiture, captured with love

Contact information, ideally using simple icons to represent email / website / facebook / instagram / pinterest

email: mira@silverlanternphotography.co.uk
website: silverlanternphotography.co.uk
facebook: @silverlanternphotography
pinterest: pinloft.com/silverlanternph
instagram: @silverlantern_photography
mobile/telephone: 07931460217

If there is too much text then please drop the instagram and pinterest information.

Font styles to use
Sans Serif

Colors
33b8a4

Requirements
Must have
• Logo
• Contact details as listed above
• sub text
Nice to have
• Instagram and Pinterest contact details
• Nice to have icons to represent website / phone / facebook etc followered by the handle where relevant

```html
<!DOCTYPE html>
<html lang="en">
<head>
<meta charset="utf-8">
<title>Silver Lantern Photography – business card</title>
<link rel="stylesheet" href="https://fonts.googleapis.com/css2?family=Questrial&family=Pinyon+Script&display=swap">
<style>
  :root {
    --teal: #33b8a4;
    --white: #ffffff;
    --paper: #f4f4f4;
    --charcoal: #353535;
    --backdrop: #1f1f1f;
    --ink: #2a2a2a;
    --contact-text: #e6e6e6;
  }
  * { box-sizing: border-box; margin: 0; padding: 0; }
  html, body {
    width: 1200px; height: 873px; overflow: hidden;
    background: var(--backdrop);
  }
  .stage {
    width: 1200px; height: 873px;
    display: flex; align-items: center; justify-content: center;
  }
  .card {
    position: relative;
    width: 900px; height: 514px;
    background: linear-gradient(180deg, var(--white), var(--paper));
    overflow: hidden;
    box-shadow: 0 20px 50px rgba(0,0,0,.55);
    font-family: "Questrial", sans-serif;
  }
  .card__waves { position: absolute; inset: 0; }
  .brand {
    position: absolute; left: 80px; top: 88px; width: 490px;
    text-align: center;
  }
  .brand__name {
    color: var(--teal);
    font-size: 36px; font-weight: 400; line-height: 1.1;
    letter-spacing: 1px;
    white-space: nowrap;
  }
  .brand__tagline {
    display: flex; align-items: center; gap: 14px;
    margin-top: 22px;
    font-family: "Pinyon Script", cursive;
    font-size: 26px; color: var(--ink);
    white-space: nowrap;
  }
  .brand__tagline::before, .brand__tagline::after {
    content: ""; flex: 1; height: 2px; background: var(--teal);
  }
  .contacts {
    position: absolute; left: 46px; top: 318px;
    list-style: none;
  }
  .contacts__item {
    display: flex; align-items: center; gap: 14px;
    height: 34px;
    color: var(--contact-text);
    font-size: 20px; letter-spacing: .3px;
  }
  .contacts__icon { width: 20px; height: 20px; flex: none; }
  .website {
    position: absolute; right: 48px; top: 352px;
    color: var(--teal);
    font-size: 21px; font-weight: 400; letter-spacing: .5px;
  }
</style>
</head>
<body>
<main class="stage">
  <article class="card">
    <svg class="card__waves" viewBox="0 0 900 514" width="900" height="514" aria-hidden="true">
      <path fill="var(--teal)" d="M0,300 C220,215 470,230 900,130 L900,514 L0,514 Z"/>
      <path fill="var(--charcoal)" d="M0,322 C240,245 480,255 900,160 L900,514 L0,514 Z"/>
      <circle cx="700" cy="170" r="96" fill="var(--white)" stroke="var(--teal)" stroke-width="7"/>
    </svg>

    <header class="brand">
      <h1 class="brand__name">Silver Lantern Photography</h1>
      <p class="brand__tagline">Family Portraiture. Captured with Love</p>
    </header>

    <ul class="contacts">
      <li class="contacts__item">
        <svg class="contacts__icon" viewBox="0 0 20 20" aria-hidden="true"><path fill="var(--teal)" d="M2 7c0-3 3-4 8-4s8 1 8 4v1h-4V6.5c-1-.6-7-.6-8 0V8H2zM5 9h10l2 8H3z"/><circle cx="10" cy="13" r="2" fill="var(--charcoal)"/></svg>
        <span>07931460217</span>
      </li>
      <li class="contacts__item">
        <svg class="contacts__icon" viewBox="0 0 20 20" aria-hidden="true"><rect x="1" y="4" width="18" height="12" rx="1" fill="var(--teal)"/><path d="M2 5l8 6 8-6" fill="none" stroke="var(--charcoal)" stroke-width="1.6"/></svg>
        <span>mira@silverlanternphotography.co.uk</span>
      </li>
      <li class="contacts__item">
        <svg class="contacts__icon" viewBox="0 0 20 20" aria-hidden="true"><circle cx="10" cy="10" r="8" fill="var(--teal)"/></svg>
        <span>@silverlanternphotography</span>
      </li>
      <li class="contacts__item">
        <svg class="contacts__icon" viewBox="0 0 20 20" aria-hidden="true"><circle cx="10" cy="10" r="8" fill="var(--teal)"/></svg>
        <span>pinloft.com/silverlanternph</span>
      </li>
      <li class="contacts__item">
        <svg class="contacts__icon" viewBox="0 0 20 20" aria-hidden="true"><circle cx="10" cy="10" r="8" fill="var(--teal)"/></svg>
        <span>@silverlantern_photography</span>
      </li>
    </ul>

    <p class="website">www.silverlanternphotography.co.uk</p>
  </article>
</main>
</body>
</html>
```